indépendant en tant que Massothérapeute et Préparateur Mental, j'ai besoin de ...

Massothérapeute et préparateur mental indépendant, je recherche une carte de visite sobre et dynamique, sans images liées au massage ou à la préparation mentale mais intégrant mon logo. Les couleurs que j'aime bien sont : Blanc, gris, anthracite, noir et jaune

Contact Information for Business Card

carte de préférence Horizontale
neutre qui puisse toucher le deux domaines Massothérapie et préparation mentale

Requirements
Must have
• mon projet doit intégrer au recto:
LOGO
Loïc Vermande
078 315 26 49
info@loicvermande-exemple.ch
et éventuellement www.loicvermande-exemple.ch

et au verso les deux adresses:

Chemin des Ormelets 27B
1400 Yverdon-les-Bains

Rue des Tanneries 9
1700 Fribourg

Should not have
• mon projet ne doit pas contenir d'image en liens avec le massage ni la préparation mentale.

```html
<!DOCTYPE html>
<html lang="fr">
<head>
<meta charset="utf-8">
<title>Loïc Vermande – Cartes de visite</title>
<link href="https://fonts.googleapis.com/css2?family=Crimson+Pro:wght@400;600;700&family=Montserrat:wght@500&display=swap" rel="stylesheet">
<style>
  :root {
    --bg: #2a2a2b;
    --card: #5e5e60;
    --card-edge: #1d1b1c;
    --ink: #1f1e20;
    --ink-soft: #2e2d30;
    --rule: #3a393c;
  }
  * { margin: 0; padding: 0; box-sizing: border-box; }
  html, body { width: 1200px; height: 900px; overflow: hidden; }
  body {
    background: var(--bg);
    position: relative;
    font-family: "Crimson Pro", Georgia, serif;
    color: var(--ink);
  }
  .card {
    position: absolute;
    width: 580px;
    height: 375px;
    background: var(--card);
    border: 9px solid var(--card-edge);
    border-radius: 3px;
    box-shadow: 0 14px 30px rgba(0,0,0,.45);
  }
  .card--back { left: 60px; top: 50px; }
  .card--front { left: 560px; top: 465px; }

  .brand { display: flex; align-items: center; gap: 10px; }
  .brand__dot { width: 14px; height: 14px; background: var(--ink); border-radius: 50%; }
  .brand__text { display: flex; flex-direction: column; }
  .brand__name { font-weight: 700; font-size: 30px; line-height: 1; color: var(--ink); }
  .brand__role {
    font-family: "Montserrat", Arial, sans-serif;
    font-weight: 500; font-size: 9.5px; letter-spacing: .6px;
    text-transform: uppercase; color: var(--ink); margin-top: 4px;
  }

  /* back */
  .back__rule { position: absolute; height: 1px; background: var(--rule); }
  .back__rule--top { right: 0; width: 300px; top: 118px; }
  .back__rule--bottom { left: 210px; right: 18px; top: 205px; }
  .card--back .brand { position: absolute; right: 32px; top: 138px; }
  .addresses { position: absolute; right: 32px; top: 222px; text-align: right; font-size: 19px; line-height: 1.55; color: var(--ink-soft); }
  .address { display: flex; justify-content: flex-end; align-items: center; gap: 8px; }
  .icon { width: 14px; height: 14px; fill: var(--ink-soft); flex: none; }

  /* front */
  .card--front .brand { position: absolute; left: 28px; top: 34px; }
  .front__mark {
    position: absolute; right: 30px; top: 140px;
    font-weight: 700; font-size: 46px; line-height: 1; color: #8a8a8d;
  }
  .holder { position: absolute; left: 60px; top: 218px; font-weight: 700; font-size: 26px; color: var(--ink); }
  .contacts { position: absolute; left: 60px; top: 258px; list-style: none; font-size: 19px; line-height: 1.5; color: var(--ink-soft); }
  .contacts li { display: flex; align-items: center; gap: 10px; }
</style>
</head>
<body>

<section class="card card--back" aria-label="Verso">
  <div class="back__rule back__rule--top"></div>
  <div class="brand">
    <span class="brand__dot"></span>
    <div class="brand__text">
      <span class="brand__name">Loïc Vermande</span>
      <span class="brand__role">Massothérapeute / Préparateur Mental</span>
    </div>
  </div>
  <div class="back__rule back__rule--bottom"></div>
  <div class="addresses">
    <p class="address">Chemin des Ormelets 27B, 1400 Yverdon-les-Bains
      <svg class="icon" viewBox="0 0 24 24"><path d="M12 2a7 7 0 0 0-7 7c0 5 7 13 7 13s7-8 7-13a7 7 0 0 0-7-7zm0 9.5A2.5 2.5 0 1 1 12 6.5a2.5 2.5 0 0 1 0 5z"/></svg>
    </p>
    <p class="address">Rue des Tanneries 9, 1700 Fribourg
      <svg class="icon" viewBox="0 0 24 24"><path d="M12 2a7 7 0 0 0-7 7c0 5 7 13 7 13s7-8 7-13a7 7 0 0 0-7-7zm0 9.5A2.5 2.5 0 1 1 12 6.5a2.5 2.5 0 0 1 0 5z"/></svg>
    </p>
  </div>
</section>

<section class="card card--front" aria-label="Recto">
  <div class="brand">
    <span class="brand__dot"></span>
    <div class="brand__text">
      <span class="brand__name">Loïc Vermande</span>
      <span class="brand__role">Massothérapeute / Préparateur Mental</span>
    </div>
  </div>
  <div class="front__mark">Loïc Vermande</div>
  <p class="holder">Loïc Vermande</p>
  <ul class="contacts">
    <li><svg class="icon" viewBox="0 0 24 24"><path d="M6.6 10.8a15 15 0 0 0 6.6 6.6l2.2-2.2a1 1 0 0 1 1-.25 11.4 11.4 0 0 0 3.6.57 1 1 0 0 1 1 1V20a1 1 0 0 1-1 1A17 17 0 0 1 3 4a1 1 0 0 1 1-1h3.5a1 1 0 0 1 1 1c0 1.25.2 2.45.57 3.57a1 1 0 0 1-.25 1z"/></svg>078 315 26 49</li>
    <li><svg class="icon" viewBox="0 0 24 24"><path d="M3 5h18v14H3zm2 2v.5l7 4.5 7-4.5V7zm0 3v7h14v-7l-7 4.5z"/></svg>info@loicvermande-exemple.ch</li>
    <li><svg class="icon" viewBox="0 0 24 24"><circle cx="12" cy="12" r="9"/></svg>www.loicvermande-exemple.ch</li>
  </ul>
</section>

</body>
</html>
```